Wageline Associates Business Card Design

We need a business card designed around our new logo. The business card should be modern in design & should communicate success, confidence, power, sophistication. The target market is young business professionals. This is for a human resource & payroll outsourcing business.

```html
<!DOCTYPE html>
<html lang="en">
<head>
<meta charset="utf-8">
<title>Wageline Associates Business Cards</title>
<link href="https://fonts.googleapis.com/css2?family=Libre+Baskerville:ital,wght@0,400;0,700;1,400&family=Open+Sans:wght@400;600&display=swap" rel="stylesheet">
<style>
  :root {
    --bg: #8f8f8f;
    --card: #ffffff;
    --ink: #1a1a1a;
    --red: #e01e25;
    --black: #111111;
    --rule: #9a9a9a;
    --white: #ffffff;
  }
  * { margin: 0; padding: 0; box-sizing: border-box; }
  html, body {
    width: 1200px; height: 900px; overflow: hidden;
    background: radial-gradient(circle at 50% 35%, #b4b4b4 0%, var(--bg) 70%);
  }
  .card {
    position: absolute;
    width: 540px; height: 310px;
    background: var(--card);
    border-radius: 18px;
    overflow: hidden;
    box-shadow: 0 14px 30px rgba(0,0,0,0.3);
  }
  .card--back { left: 30px; top: 295px; }
  .card--front { left: 630px; top: 295px; }

  .brand {
    position: absolute;
    font-family: "Libre Baskerville", serif;
    font-weight: 700;
    color: var(--ink);
    line-height: 1;
    text-align: right;
  }
  .brand__main { display: block; }
  .brand__sub { display: block; }

  .card--front .brand { left: 150px; top: 70px; }
  .card--front .brand__main { font-size: 44px; }
  .card--front .brand__sub { font-size: 22px; margin-top: 8px; }

  .band { position: absolute; height: 40px; }
  .band--red { background: var(--red); }
  .band--black { background: var(--black); }
  .band__text {
    font-family: "Open Sans", sans-serif;
    color: var(--white);
    font-size: 13px;
    line-height: 40px;
    white-space: nowrap;
  }

  .card--front .band--left { top: 205px; left: 0; width: 170px; clip-path: polygon(0 0, 100% 0, 88% 100%, 0 100%); }
  .card--front .band--mid { top: 215px; left: 150px; width: 290px; height: 30px; clip-path: polygon(7% 0, 100% 0, 93% 100%, 0 100%); text-align: center; }
  .card--front .band--mid .band__text { line-height: 30px; letter-spacing: 3px; font-size: 12px; }
  .card--front .band--right { top: 205px; left: 420px; width: 120px; clip-path: polygon(14% 0, 100% 0, 100% 100%, 0 100%); }

  .person { position: absolute; left: 40px; top: 34px; }
  .person__name {
    font-family: "Libre Baskerville", serif; font-weight: 700;
    font-size: 22px; color: var(--ink);
  }
  .person__title {
    font-family: "Libre Baskerville", serif; font-style: italic;
    font-size: 12px; color: var(--red); margin-top: 4px;
  }
  .person__rule { position: absolute; left: 40px; top: 92px; width: 110px; height: 3px; background: var(--red); }
  .connector { position: absolute; left: 0; top: 0; }

  .contacts {
    position: absolute; left: 44px; top: 118px; list-style: none;
    font-family: "Open Sans", sans-serif; font-size: 13px; color: var(--ink);
  }
  .contacts li { display: flex; align-items: center; gap: 10px; height: 22px; }
  .contacts svg { width: 12px; height: 12px; }

  .card--back .brand { left: 300px; top: 150px; }
  .card--back .brand__main { font-size: 30px; }
  .card--back .brand__sub { font-size: 16px; margin-top: 4px; }

  .card--back .band--address { top: 245px; left: 0; width: 300px; clip-path: polygon(0 0, 100% 0, 94% 100%, 0 100%); padding-left: 24px; }
  .card--back .band--address .band__text { font-size: 12px; }
  .card--back .band--social { top: 245px; left: 286px; width: 254px; clip-path: polygon(7% 0, 100% 0, 100% 100%, 0 100%); padding-left: 34px; display: flex; align-items: center; gap: 8px; }
  .social-mark { width: 16px; height: 16px; background: var(--red); border-radius: 3px; }
</style>
</head>
<body>
  <section class="card card--back" aria-label="Business card, contact side">
    <div class="person">
      <div class="person__name">Your Name</div>
      <div class="person__title">Job Title</div>
    </div>
    <div class="person__rule"></div>
    <svg class="connector" width="540" height="310" aria-hidden="true">
      <line x1="150" y1="93" x2="295" y2="168" stroke="var(--rule)" stroke-width="1"/>
    </svg>
    <ul class="contacts">
      <li>
        <svg viewBox="0 0 12 12"><path d="M2 1 L4.5 1 L5.5 3.5 L4 4.5 Q5 7 7.5 8 L8.5 6.5 L11 7.5 L11 10 Q6 11 2 6 Q1 3 2 1Z" fill="var(--red)"/></svg>
        <span>000 000 0000</span>
      </li>
      <li>
        <svg viewBox="0 0 12 12"><rect x="1" y="2.5" width="10" height="7" rx="1" fill="var(--red)"/><path d="M1.5 3 L6 6.5 L10.5 3" stroke="#fff" stroke-width="0.9" fill="none"/></svg>
        <span>youremail@xyz.com</span>
      </li>
      <li>
        <svg viewBox="0 0 12 12"><circle cx="6" cy="6" r="5" fill="var(--red)"/><path d="M1 6 H11 M6 1 Q3 6 6 11 M6 1 Q9 6 6 11" stroke="#fff" stroke-width="0.8" fill="none"/></svg>
        <span>www.yourwebsite.com</span>
      </li>
    </ul>
    <div class="brand">
      <span class="brand__main">Wageline</span>
      <span class="brand__sub">Associates</span>
    </div>
    <div class="band band--red band--address"><span class="band__text">000, Anywhere, Somewhere, City, ST 0000</span></div>
    <div class="band band--black band--social">
      <span class="band__text">Wagelineassociates/</span>
      <span class="social-mark"></span>
      <span class="social-mark"></span>
    </div>
  </section>

  <section class="card card--front" aria-label="Business card, logo side">
    <div class="brand">
      <span class="brand__main">Wageline</span>
      <span class="brand__sub">Associates</span>
    </div>
    <div class="band band--red band--left"></div>
    <div class="band band--black band--mid"><span class="band__text">www.yourwebsite.com</span></div>
    <div class="band band--red band--right"></div>
  </section>
</body>
</html>
```